Brightfold Partners Website

Brightfold Partners (BP) provide Analytics & Enterprise Performance Management (EPM) advisory & consultancy services. We are passionate about data and making a difference for our clients by working in partnership with them, helping them on their journey to becoming an Brightfold Partner. We deliver insights which give our clients a competitive edge and a much deeper understanding of their organisation.

We need a website which shows who we are, what we do and how we do it.

www.brightfold-partners.example is our very basic website at the moment. We want to completely revamp it with a corporate look

```html
<!DOCTYPE html>
<html lang="en">
<head>
<meta charset="utf-8">
<title>Brightfold Partners</title>
<link rel="stylesheet" href="https://fonts.googleapis.com/css2?family=Poppins:wght@300;400;500;600&family=Open+Sans:wght@400&display=swap">
<style>
:root{
  --navy:#2b5473;
  --navy-dark:#234a66;
  --text:#5d6b78;
  --muted:#8a97a3;
  --pale:#f2f6fa;
  --white:#ffffff;
}
*{margin:0;padding:0;box-sizing:border-box}
html,body{width:1200px;height:3377px;overflow:hidden}
body{font-family:"Poppins",sans-serif;color:var(--text);background:var(--white);position:relative}
.abs{position:absolute}
.btn{position:absolute;display:flex;align-items:center;justify-content:center;border-radius:23px;font-weight:500;font-size:15px;height:44px}
.btn-white{background:var(--white);color:var(--navy)}
.btn-navy{background:var(--navy);color:var(--white)}
.brand{position:absolute;display:flex;align-items:center;gap:12px}
.brand-dot{width:46px;height:46px;border-radius:50%;background:var(--navy)}
.brand-name{font-weight:600;font-size:19px;line-height:21px;color:var(--navy);text-transform:uppercase;letter-spacing:.5px}

/* header */
.site-header{position:absolute;left:0;top:0;width:1200px;height:82px;background:var(--white)}
.nav{position:absolute;top:32px;left:439px;display:flex;gap:0}
.nav a{position:absolute;font-size:12.5px;font-weight:500;color:var(--navy);text-decoration:none;white-space:nowrap}
.header-phone{left:951px;top:16px;width:187px;height:52px;border-radius:26px;font-size:17px;gap:10px}

/* hero */
.hero{position:absolute;left:0;top:82px;width:1200px;height:600px;background:linear-gradient(90deg,#2f5a78 0%,#4a6f8a 45%,#7e97aa 75%,#9fb1bf 100%)}
.hero-title{left:60px;top:150px;font-size:72px;font-weight:600;line-height:80px;color:var(--white)}
.hero-sub{left:62px;top:315px;font-family:"Open Sans",sans-serif;font-size:19.5px;color:var(--white)}
.hero .btn{left:60px;top:363px;width:145px}

/* section headings */
.heading{position:absolute;left:0;width:1200px;text-align:center;font-weight:500;color:var(--navy)}

/* who */
.who-mark{left:570px;top:773px;width:60px;height:60px;border-radius:50%;background:var(--navy)}
.who-sub{left:0;width:1200px;top:903px;text-align:center;font-size:17.5px;color:var(--navy)}
.who-text{left:310px;width:580px;top:957px;text-align:center;font-size:13.5px;line-height:26px;color:var(--text)}

/* services */
.services{position:absolute;left:0;top:1189px;width:1200px;height:600px;background:linear-gradient(180deg,#4b6d87 0%,#3f6581 50%,#345a77 100%)}
.service{position:absolute;top:198px;width:340px;text-align:center;color:var(--white)}
.service-icon{width:90px;height:90px;border-radius:50%;background:var(--white);margin:0 auto;display:flex;align-items:center;justify-content:center}
.service h3{font-size:21px;font-weight:500;margin-top:14px}
.service p{font-size:13.5px;line-height:26px;margin-top:10px;font-weight:300}

/* steps */
.step{position:absolute;top:1964px;width:247px;height:255px;background:var(--pale);border-radius:4px;padding:24px 20px}
.step h3{font-size:20px;font-weight:500;color:var(--navy)}
.step p{font-size:12px;line-height:22.5px;color:var(--muted);margin-top:14px}
.step a{display:block;margin-top:20px;font-size:12.5px;font-weight:600;color:var(--navy);text-decoration:none}

/* testimonial */
.avatar{left:542px;top:2434px;width:106px;height:106px;border-radius:50%;background:radial-gradient(circle at 50% 45%,#c8b8a8 0%,#8f8a86 55%,#5f6266 100%)}
.quote-badge{left:615px;top:2426px;width:37px;height:37px;border-radius:50%;background:var(--navy);display:flex;align-items:center;justify-content:center}
.quote-text{left:275px;width:650px;top:2577px;text-align:center;font-size:13.5px;line-height:26px;color:var(--text)}
.client{left:0;width:1200px;top:2682px;text-align:center;font-size:13.5px;font-weight:600;color:var(--navy)}
.dots{left:570px;top:2744px;width:60px;height:20px}

/* cta */
.cta{position:absolute;left:0;top:2853px;width:1200px;height:270px;background:var(--navy)}
.cta h2{position:absolute;left:0;width:1200px;top:67px;text-align:center;font-size:47px;font-weight:500;color:var(--white)}
.cta-phone{position:absolute;left:383px;top:140px;display:flex;align-items:center;gap:14px;color:var(--white)}
.cta-phone strong{font-size:32px;font-weight:500;letter-spacing:.5px}
.cta-or{position:absolute;left:638px;top:166px;font-size:12px;color:var(--white)}
.cta .btn{left:670px;top:145px;width:145px}

/* footer */
.site-footer{position:absolute;left:0;top:3123px;width:1200px;height:254px;background:var(--pale)}
.copyright{left:60px;top:139px;width:220px;font-size:12px;line-height:22px;color:var(--muted)}
.copyright span{color:var(--navy)}
.foot-links a{position:absolute;left:339px;font-size:12px;color:var(--muted);text-decoration:none}
.foot-links a:first-child{color:var(--navy)}
.contact-row{position:absolute;left:615px;display:flex;gap:16px;font-size:12px;line-height:22px;color:var(--muted)}
.contact-row svg{flex:none;margin-top:4px}
.partner-badge{left:893px;top:52px;width:132px;height:30px;border-radius:3px;background:#dfe6ed}
.social{width:38px;height:38px;border-radius:50%;background:var(--navy);top:104px}
</style>
</head>
<body>

<header class="site-header">
  <div class="brand" style="left:60px;top:14px">
    <span class="brand-dot"></span>
    <span class="brand-name">Brightfold<br>Partners</span>
  </div>
  <nav class="nav">
    <a style="left:0">Home</a>
    <a style="left:72px">Who We Are</a>
    <a style="left:185px">What We Do</a>
    <a style="left:300px">How We Do</a>
    <a style="left:406px">Contact Us</a>
  </nav>
  <a class="btn btn-navy header-phone">
    <svg width="22" height="22" viewBox="0 0 24 24" fill="none" stroke="#fff" stroke-width="1.6"><path d="M5 3h4l2 5-2.5 1.5a11 11 0 0 0 6 6L16 13l5 2v4a2 2 0 0 1-2 2A16 16 0 0 1 3 5a2 2 0 0 1 2-2z"/></svg>
    01 555 0142
  </a>
</header>

<section class="hero" role="img" aria-label="Photo of two businessmen in a friendly consulting meeting at a desk">
  <h1 class="abs hero-title">Brightfold<br>Partners</h1>
  <p class="abs hero-sub">DATA ANALYTICS &amp; EPM Consulting Services</p>
  <a class="btn btn-white">Contact Us</a>
</section>

<section class="who">
  <div class="abs who-mark"></div>
  <h2 class="heading" style="top:836px;font-size:46px">Who We Are</h2>
  <p class="abs who-sub">Brightfold Partners</p>
  <p class="abs who-text">BP are a Data Analytics &amp; EPM company, specialising in the implementation and support of Business Intelligence, EPM and Data Analytics business solutions, both in the Cloud and on-premise.</p>
  <a class="btn btn-navy" style="left:527px;top:1052px;width:146px">Read More</a>
</section>

<section class="services" role="img" aria-label="Blue-tinted photo of a city skyline of skyscrapers">
  <h2 class="heading" style="top:88px;font-size:46px;color:#fff">Our Services</h2>

  <div class="service" style="left:58px">
    <div class="service-icon">
      <svg width="46" height="46" viewBox="0 0 48 48" fill="none" stroke="#2b5473" stroke-width="1.8"><circle cx="14" cy="12" r="4"/><circle cx="24" cy="10" r="4"/><circle cx="34" cy="12" r="4"/><path d="M8 30v-8a5 5 0 0 1 10 0M18 28v-8a6 6 0 0 1 12 0v8M30 22a5 5 0 0 1 10 0v8"/><path d="M6 30h36v4H6zM12 34v8M36 34v8"/></svg>
    </div>
    <h3>Advise &amp; Architect</h3>
    <p>Helping our customers understand the art of the possible and safeguarding their investments by overseeing implementations.</p>
  </div>
  <a class="btn btn-white" style="left:159px;top:445px;width:146px">Read More</a>

  <div class="service" style="left:430px">
    <div class="service-icon">
      <svg width="46" height="46" viewBox="0 0 48 48" fill="none" stroke="#2b5473" stroke-width="1.8"><path d="M24 12a9 9 0 0 0-5 16.5V33h10v-4.5A9 9 0 0 0 24 12z"/><path d="M20 37h8M21 41h6M24 4v4M10 10l3 3M38 10l-3 3"/></svg>
    </div>
    <h3>Design &amp; Implement</h3>
    <p>Working with the project management team, through each stage of the project, with clearly defined deliverables and well exercised...</p>
  </div>
  <a class="btn btn-white" style="left:527px;top:445px;width:146px">Read More</a>

  <div class="service" style="left:798px">
    <div class="service-icon">
      <svg width="46" height="46" viewBox="0 0 48 48" fill="none" stroke="#2b5473" stroke-width="1.8"><circle cx="24" cy="24" r="5"/><circle cx="24" cy="24" r="10"/><path d="M24 6v6M24 36v6M6 24h6M36 24h6M11 11l4 4M33 33l4 4M37 11l-4 4M15 33l-4 4"/></svg>
    </div>
    <h3>Optimise &amp; Manage</h3>
    <p>Our Managed Services delivers proactive, on-demand support for EPM and Data Analytics environments...</p>
  </div>
  <a class="btn btn-white" style="left:898px;top:445px;width:146px">Read More</a>
</section>

<section class="how">
  <h2 class="heading" style="top:1879px;font-size:46px">How We Do</h2>
  <article class="step" style="left:60px"><h3>Step 1</h3><p>Lorem Ipsum is simply dummy text of the printing and typesetting industry. Lorem Ipsum has been the industry's standard dummy text ever since the 1500...</p><a>READ MORE</a></article>
  <article class="step" style="left:338px"><h3>Step 2</h3><p>Lorem Ipsum is simply dummy text of the printing and typesetting industry. Lorem Ipsum has been the industry's standard dummy text ever since the 1500...</p><a>READ MORE</a></article>
  <article class="step" style="left:615px"><h3>Step 3</h3><p>Lorem Ipsum is simply dummy text of the printing and typesetting industry. Lorem Ipsum has been the industry's standard dummy text ever since the 1500...</p><a>READ MORE</a></article>
  <article class="step" style="left:892px"><h3>Step 4</h3><p>Lorem Ipsum is simply dummy text of the printing and typesetting industry. Lorem Ipsum has been the industry's standard dummy text ever since the 1500...</p><a>READ MORE</a></article>
</section>

<section class="testimonials">
  <h2 class="heading" style="top:2316px;font-size:46px">What Our Clients Say</h2>
  <div class="abs avatar" role="img" aria-label="Portrait photo of a client"></div>
  <div class="abs quote-badge">
    <svg width="16" height="14" viewBox="0 0 16 14" fill="#fff"><path d="M0 8a6 6 0 0 1 6-6v2a4 4 0 0 0-3 3h3v7H0zM9 8a6 6 0 0 1 6-6v2a4 4 0 0 0-3 3h3v7H9z"/></svg>
  </div>
  <p class="abs quote-text">Lorem Ipsum is simply dummy text of the printing and typesetting industry. Lorem Ipsum has been the industry's standard dummy text ever since the 1500s, when an unknown printer took a galley of type and scrambled it to make a type specimen book.</p>
  <p class="abs client">- Clinet Name</p>
  <svg class="abs dots" viewBox="0 0 60 20"><circle cx="7" cy="10" r="3.5" fill="#2b5473"/><circle cx="30" cy="10" r="7" fill="none" stroke="#2b5473" stroke-width="1.5"/><circle cx="30" cy="10" r="3.5" fill="#2b5473"/><circle cx="53" cy="10" r="3.5" fill="#2b5473"/></svg>
</section>

<section class="cta">
  <h2>Contact us to discuss your business needs</h2>
  <div class="cta-phone">
    <svg width="46" height="46" viewBox="0 0 48 48" fill="none" stroke="#fff" stroke-width="1.6"><path d="M8 14h5l3 7-3 2a16 16 0 0 0 8 8l2-3 7 3v5a3 3 0 0 1-3 3A24 24 0 0 1 5 17a3 3 0 0 1 3-3z"/><path d="M26 6a16 16 0 0 1 16 16"/><text x="27" y="25" font-size="11" fill="#fff" stroke="none" font-family="Poppins,sans-serif">24</text></svg>
    <strong>01 555 0142</strong>
  </div>
  <span class="cta-or">Or</span>
  <a class="btn btn-white">Contact Us</a>
</section>

<footer class="site-footer">
  <div class="brand" style="left:60px;top:50px">
    <span class="brand-dot" style="width:56px;height:56px"></span>
    <span class="brand-name" style="font-size:20px;line-height:22px">Brightfold<br>Partners</span>
  </div>
  <p class="abs copyright">© <span>Brightfold Partners</span> - 2022. All Rights Reserved.</p>

  <nav class="foot-links">
    <a style="top:61px">Home</a>
    <a style="top:91px">Who we Are</a>
    <a style="top:121px">What We Do</a>
    <a style="top:151px">How We Do</a>
    <a style="top:181px">Contact Us</a>
  </nav>

  <div class="contact-row" style="top:57px">
    <svg width="14" height="12" viewBox="0 0 14 12" fill="#2b5473"><path d="M0 0h14v12H0z"/><path d="M0 1l7 5 7-5" stroke="#f2f6fa" stroke-width="1.3" fill="none"/></svg>
    <span>12 Harbour Row, Dockside,<br>Dublin 4, D04 Q7K2</span>
  </div>
  <div class="contact-row" style="top:114px">
    <svg width="14" height="14" viewBox="0 0 24 24" fill="#2b5473"><path d="M5 2h4l2 6-3 2a12 12 0 0 0 6 6l2-3 6 2v4a3 3 0 0 1-3 3A19 19 0 0 1 2 5a3 3 0 0 1 3-3z"/></svg>
    <span>01 555 0142</span>
  </div>
  <div class="contact-row" style="top:157px">
    <svg width="14" height="16" viewBox="0 0 14 18" fill="#2b5473"><path d="M7 0a7 7 0 0 1 7 7c0 5-7 11-7 11S0 12 0 7a7 7 0 0 1 7-7z"/><circle cx="7" cy="7" r="2.5" fill="#f2f6fa"/></svg>
    <span>info@brightfold-partners.example</span>
  </div>

  <div class="abs partner-badge" role="img" aria-label="Technology partner badge"></div>
  <a class="abs social" style="left:892px" aria-label="Professional network profile"></a>
  <a class="abs social" style="left:944px" aria-label="Social feed profile"></a>
</footer>

</body>
</html>
```